Make my Savory Fungi Strips sell!!

Design for a new mushroom jerky product.
The meatiest (no) beef jerky ever!!
Bite it! Rip it! Tear it! Chew it! There is nothing meatier! Not even meat!
Please use our company logo (supplied) somewhere on the package. It does not have to be the focus. Just anywhere in the design.
Not sure if I want to focus on the plant based, healthy, clean - eating design or a masculine, taste based, BBQ, design. Surprise me!
Will be used on a stand up pouch, with a window.

Target Market(s)

Jerky lovers. Plant based connoisseurs. Vegans. Millenials. People that want a true meat experience without the cruelty.

Requirements
Must have
• Verdant Grove Foods logo.
Nice to have
• Mushrooms, shiitake, nature, muscles, happy cows?,
Should not have
• The word vegan. Stick to Plant Based.

```html
<!DOCTYPE html>
<html lang="en">
<head>
<meta charset="utf-8">
<title>Savory Fungi Strips – Pouch Front</title>
<link rel="stylesheet" href="https://fonts.googleapis.com/css2?family=Big+Shoulders+Display:wght@500&family=Arimo:wght@400;700&display=swap">
<style>
  :root {
    --bg: #e4e4e4;
    --pouch: #ffffff;
    --bark: #4a2914;
    --leaf: #6bb130;
    --fungus-light: #ddd0c2;
    --fungus-dark: #b9a08a;
  }
  * { margin: 0; padding: 0; box-sizing: border-box; }
  html, body { width: 1200px; height: 840px; overflow: hidden; }
  body {
    background: var(--bg);
    font-family: "Arimo", Arial, sans-serif;
    position: relative;
  }
  .pouch-front {
    position: absolute;
    left: 382px; top: 70px;
    width: 436px; height: 706px;
    background: var(--pouch);
    overflow: hidden;
  }
  .top-band {
    position: absolute; left: 0; top: 0;
    width: 100%; height: 96px;
    background: var(--bark);
  }
  .maker-mark {
    position: absolute; top: 40px; left: 0; width: 100%;
    display: flex; justify-content: center; align-items: center; gap: 7px;
    color: var(--leaf);
    font-weight: 700; font-size: 12px; letter-spacing: 0.5px;
  }
  .maker-mark .dot {
    width: 12px; height: 12px; border-radius: 50%;
    background: var(--leaf);
  }
  .brand-name {
    position: absolute; left: 48px; top: 146px;
    color: var(--leaf);
    font-size: 17px; letter-spacing: 0.3px;
  }
  .product-title {
    position: absolute; left: 50px; top: 167px;
    font-family: "Big Shoulders Display", "Arial Narrow", sans-serif;
    font-weight: 500;
    font-size: 108px; line-height: 121px;
    color: var(--bark);
    letter-spacing: 6px;
    text-transform: uppercase;
  }
  .action-list {
    position: absolute; right: 66px; top: 455px;
    list-style: none; text-align: right;
    color: var(--leaf);
    font-weight: 700; font-size: 19px; line-height: 27px;
  }
  .fungi-art {
    position: absolute; left: 22px; top: 560px;
    width: 400px; height: 146px;
    background: linear-gradient(180deg, var(--fungus-light) 0%, var(--fungus-dark) 100%);
    border-radius: 70px 90px 0 0;
  }
  .claim {
    position: absolute; left: 0; top: 632px; width: 100%;
    text-align: center;
    color: var(--bark);
    font-weight: 700; font-size: 13px;
  }
  .net-weight {
    position: absolute; left: 0; top: 658px; width: 100%;
    text-align: center;
    color: var(--bark);
    font-size: 19px;
  }
  .bottom-band {
    position: absolute; left: 0; bottom: 0;
    width: 100%; height: 20px;
    background: var(--bark);
  }
</style>
</head>
<body>
  <main class="pouch-front">
    <div class="top-band"></div>
    <div class="maker-mark"><span class="dot"></span>VERDANT GROVE FOODS</div>

    <p class="brand-name">VERDANT GROVE FOODS</p>
    <h1 class="product-title">Savory<br>Fungi<br>Strips</h1>

    <ul class="action-list">
      <li>BITE IT!</li>
      <li>RIP IT!</li>
      <li>TEAR IT!</li>
      <li>CHEW IT!</li>
    </ul>

    <div class="fungi-art" role="img" aria-label="Illustration of a cluster of mushrooms with speckled caps"></div>

    <p class="claim">THERE IS NOTHING MEATIER! NOT EVEN MEAT!</p>
    <p class="net-weight">NET WT.&nbsp; <b>2.2 oz (62 g)</b></p>
    <div class="bottom-band"></div>
  </main>
</body>
</html>
```